Business Card Design Project

Hi,

We are a new modern sheet metal business and I require a business card for our sales reps.

The card should be double sided and standout in a crowd.

I have attached our logo and our website is www.folvik.com.au.

Please ask if you have any further questions
Updates

hi everyone, 

I'm wondering if we can try to lighten the cards mood.  Everyone is using black and I'm not sure how that would be accepted in real life.

Gregory

Reason: Still No receiving what I was hoping for.

Industry/Entity Type

Business

Requirements
Must have
• double sided

```html
<!DOCTYPE html>
<html lang="en">
<head>
<meta charset="utf-8">
<title>Folvik Sheetmetal – Business Card</title>
<link rel="stylesheet" href="https://fonts.googleapis.com/css2?family=Arimo:wght@400;700&display=swap">
<style>
  :root {
    --stage: #e9e9ec;
    --navy: #1f2a86;
    --blue: #2b3b9a;
    --blue-light: #3a4cb0;
    --blue-dark: #1a2470;
    --white: #ffffff;
    --panel: #f2f2f3;
    --grey-text: #6d6d72;
    --rule: #c9c9cf;
  }
  * { box-sizing: border-box; margin: 0; padding: 0; }
  html, body {
    width: 1200px; height: 834px; overflow: hidden;
    background: var(--stage);
    font-family: "Arimo", Arial, sans-serif;
  }
  .stage {
    position: relative; width: 1200px; height: 834px;
    display: flex; align-items: center; justify-content: center; gap: 40px;
  }
  .card {
    position: relative; width: 540px; height: 330px; overflow: hidden;
    box-shadow: 0 10px 30px rgba(0,0,0,.18);
  }
  .card-facets { position: absolute; inset: 0; width: 100%; height: 100%; }

  /* Front */
  .card-front { background: var(--blue); color: var(--white); }
  .front-web {
    position: absolute; left: 22px; top: 50%;
    transform: translate(-50%, -50%) rotate(-90deg) translateY(50%);
    transform-origin: center;
    font-size: 11px; letter-spacing: .5px; color: rgba(255,255,255,.75);
    white-space: nowrap;
  }
  .brand { position: absolute; display: flex; flex-direction: column; }
  .brand-name { font-weight: 700; font-size: 52px; line-height: .9; letter-spacing: -1px; }
  .brand-sub { font-weight: 700; font-size: 15px; letter-spacing: 6px; margin-top: 4px; }
  .brand-tagline { font-size: 10px; margin-top: 8px; letter-spacing: .3px; }
  .card-front .brand { left: 175px; top: 112px; color: var(--white); }

  /* Back */
  .card-back { background: var(--white); }
  .back-panel {
    position: absolute; right: 0; top: 0; width: 46%; height: 100%;
    background: var(--panel); border-left: 1px solid #e2e2e4;
  }
  .card-back .brand { left: 38px; top: 40px; color: var(--navy); }
  .card-back .brand-tagline { color: var(--navy); }
  .contact {
    position: absolute; right: 28px; top: 178px; width: 200px; color: var(--grey-text);
  }
  .contact-web { color: var(--navy); font-size: 15px; font-weight: 400; }
  .contact-address { font-size: 8.5px; line-height: 1.35; margin-top: 3px; border-bottom: 1px solid var(--rule); padding-bottom: 4px; }
  .contact-line { display: flex; align-items: baseline; gap: 10px; font-size: 20px; line-height: 1.15; margin-top: 2px; }
  .contact-label { color: var(--navy); font-weight: 700; font-size: 18px; width: 14px; }
</style>
</head>
<body>
<main class="stage">

  <section class="card card-front" aria-label="Card front">
    <svg class="card-facets" viewBox="0 0 540 330" aria-hidden="true">
      <polygon points="0,0 540,0 540,40 60,40 40,0" fill="var(--blue-light)" opacity=".45"/>
      <polygon points="0,230 60,230 80,330 0,330" fill="var(--blue-dark)" opacity=".35"/>
      <polygon points="60,40 540,40 540,330 80,330 60,230" fill="var(--blue)"/>
      <polygon points="0,0 40,0 60,40 60,230 0,230" fill="var(--blue-light)" opacity=".25"/>
    </svg>
    <p class="front-web">www.folvik.com.au</p>
    <div class="brand">
      <span class="brand-name">FOLVIK</span>
      <span class="brand-sub">SHEETMETAL</span>
      <span class="brand-tagline">Flashings | Gutter | Rainwater Goods</span>
    </div>
  </section>

  <section class="card card-back" aria-label="Card back">
    <div class="back-panel"></div>
    <svg class="card-facets" viewBox="0 0 540 330" aria-hidden="true">
      <polygon points="30,330 60,265 250,265 290,330" fill="var(--navy)"/>
      <polygon points="250,265 290,330 290,290" fill="var(--blue-dark)"/>
    </svg>
    <div class="brand">
      <span class="brand-name">FOLVIK</span>
      <span class="brand-sub">SHEETMETAL</span>
      <span class="brand-tagline">Flashings | Gutter | Rainwater Goods</span>
    </div>
    <address class="contact">
      <p class="contact-web">www.folvik.com.au</p>
      <p class="contact-address">22 Quarry Road Redbank Q 4301<br>PO Box 318 Redbank Q 4301</p>
      <p class="contact-line"><span class="contact-label">P</span>3555 0142</p>
      <p class="contact-line"><span class="contact-label">F</span>3555 0187</p>
    </address>
  </section>

</main>
</body>
</html>
```